Business Card Design

Brambledown Pantry is the name of my health coaching business. My tag line is "Where good health meets real life." I will be working with clients one-on-one and in groups. My target clients are women "of a certain age" who want to be more comfortable in their own skin. We will work together in a 6-month program. The coaching sessions will take place in my kitchen. I will also be conducting monthly cooking classes and field trips - to farmer's markets, speciality markets etc.. for my clients.
Updates

the business name is Brambledown Pantry - I'm not sure how the p got in there at the end of the name

Thank you

Please include the website - www.brambledownpantry-example.com and the tag line:

Where good health meets real life on the business card.

Thank you

Please add the phone number to the business card - sorry, I forgot to state that in the original brief

(555) 274-8150

Target Market(s)

Women "of a certain age" who want to be more comfortable in their own skin

Industry/Entity Type

Cooking

Contact Information for Business Card

Brambledown Pantry
Where good health meets real life

Rosalind Hartwell
Health Coach
(555) 274-8150

Font styles to use
Serif
Sans Serif

Requirements
Must have
• front & back design
I typical like soft colors - and have tended toward greens over time - I'm open although I would not like bright reds, yellows etc..

```html
<!DOCTYPE html>
<html lang="en">
<head>
<meta charset="utf-8">
<title>Brambledown Pantry – Business Card</title>
<link href="https://fonts.googleapis.com/css2?family=Almendra&family=Cormorant+Garamond:ital,wght@1,500;1,600&family=Arimo&display=swap" rel="stylesheet">
<style>
  :root {
    --green-deep: #4f7a54;
    --green-mid: #64906a;
    --green-soft: #77a37b;
    --streak-light: rgba(255, 255, 255, 0.05);
    --streak-dark: rgba(30, 60, 34, 0.07);
    --band-dark: rgba(40, 70, 44, 0.55);
    --band-light: rgba(220, 235, 220, 0.45);
    --ink: #ffffff;
    --shadow: rgba(20, 40, 22, 0.75);
  }
  html, body {
    margin: 0;
    padding: 0;
    width: 1200px;
    height: 702px;
    overflow: hidden;
    background: #ffffff;
  }
  .card {
    position: relative;
    width: 1200px;
    height: 702px;
    overflow: hidden;
    color: var(--ink);
  }
  .card__texture {
    position: absolute;
    inset: 0;
    background:
      repeating-linear-gradient(90deg, var(--streak-light) 0 3px, transparent 3px 9px, var(--streak-dark) 9px 12px, transparent 12px 21px),
      linear-gradient(90deg, var(--green-mid) 0%, var(--green-soft) 35%, var(--green-mid) 60%, var(--green-deep) 100%);
  }
  .card__band-highlight {
    position: absolute;
    left: 0;
    right: 0;
    top: 265px;
    height: 24px;
    background: linear-gradient(180deg, rgba(255,255,255,0.1), var(--band-light), rgba(255,255,255,0.1));
  }
  .card__band {
    position: absolute;
    left: 0;
    right: 0;
    top: 289px;
    height: 109px;
    background: linear-gradient(180deg, var(--band-dark) 0%, rgba(40,70,44,0.45) 80%, rgba(30,55,34,0.7) 100%);
  }
  .business-name {
    position: absolute;
    left: 0;
    right: 0;
    top: 70px;
    margin: 0;
    text-align: center;
    font-family: "Almendra", serif;
    font-weight: 400;
    font-size: 116px;
    line-height: 1;
    letter-spacing: 2px;
    text-shadow: 4px 5px 6px var(--shadow);
  }
  .tagline {
    position: absolute;
    left: 0;
    right: 0;
    top: 300px;
    margin: 0;
    text-align: center;
    font-family: "Cormorant Garamond", serif;
    font-style: italic;
    font-weight: 600;
    font-size: 68px;
    line-height: 1;
    letter-spacing: 3px;
    text-shadow: 2px 3px 4px var(--shadow);
  }
  .contact {
    position: absolute;
    left: 77px;
    top: 540px;
    margin: 0;
    font-family: "Arimo", sans-serif;
    font-size: 29px;
    line-height: 42px;
    text-shadow: 1px 2px 3px var(--shadow);
  }
  .contact__phone, .contact__website { display: block; }
  .coach {
    position: absolute;
    left: 688px;
    width: 460px;
    top: 518px;
    margin: 0;
    text-align: center;
    font-family: "Cormorant Garamond", serif;
    font-style: italic;
    font-weight: 600;
    font-size: 44px;
    line-height: 56px;
    letter-spacing: 2px;
    text-shadow: 2px 3px 4px var(--shadow);
  }
  .coach__name, .coach__title { display: block; }
</style>
</head>
<body>
  <main class="card">
    <div class="card__texture" role="img" aria-label="Soft green streaked paper texture background"></div>
    <div class="card__band-highlight"></div>
    <div class="card__band"></div>

    <h1 class="business-name">Brambledown Pantry</h1>
    <p class="tagline">Where good health meets real life</p>

    <p class="coach">
      <span class="coach__name">Rosalind Hartwell</span>
      <span class="coach__title">Health Coach</span>
    </p>

    <p class="contact">
      <span class="contact__phone">(555) 274-8150</span>
      <span class="contact__website">www.brambledownpantry-example.com</span>
    </p>
  </main>
</body>
</html>
```